General Dental Office Business Card

I run a private general dental office in southern California, and would like a refresh/redesign of my business card. I focus on quality care rather than volume. The email address on the uploaded current card should be updated to: info@marbleshoredental.example. The current card's logo is a deboss, but I am open to other ideas. The logo can be refreshed, but it is something that's been with me since the beginning of the office, so I wouldn't want a drastic redesign.
Target Market(s)
Adults 18-99, whoever needs dental services
Industry/Entity Type
Healthcare/Dental
Contact Information for Business Card
Name, Address, Phone, email
Colors
Designer to choose colors to be used in the design.
Requirements
Must have
- Logo (Same as original one in the uploaded file), space on back for appointment time/date

```html
<!DOCTYPE html>
<html lang="en">
<head>
<meta charset="utf-8">
<title>Marble Shore Dental — Business Card</title>
<link rel="stylesheet" href="https://fonts.googleapis.com/css2?family=Source+Sans+3:ital,wght@0,400;0,600;1,400&display=swap">
<style>
  :root {
    --bg: #ececec;
    --card: #ffffff;
    --brand: #7fd3e8;
    --brand-faint: #f0f9fc;
    --ink: #222222;
    --muted: #7a7a7a;
    --rule: #b8b8b8;
  }
  * { margin: 0; padding: 0; box-sizing: border-box; }
  html, body { width: 1093px; height: 1200px; overflow: hidden; }
  body {
    background: var(--bg);
    font-family: "Source Sans 3", "Myriad Pro", sans-serif;
    position: relative;
  }
  .card {
    position: absolute;
    background: var(--card);
    border-radius: 24px;
    box-shadow: 0 3px 8px rgba(0,0,0,0.12);
    overflow: hidden;
  }
  .card-front { left: 265px; top: 226px; width: 576px; height: 356px; }
  .card-back  { left: 265px; top: 621px; width: 581px; height: 356px; }

  .abs { position: absolute; line-height: 1; white-space: nowrap; }

  /* front */
  .brand-circle {
    position: absolute; left: 95px; top: 95px; width: 116px; height: 116px;
    border: 6px solid var(--brand); border-radius: 50%;
  }
  .brand-name { left: 42px; top: 242px; font-size: 28px; color: var(--brand); }
  .divider {
    position: absolute; left: 284px; top: 74px; width: 1.5px; height: 209px;
    background: var(--rule);
  }
  .doctor { left: 304px; top: 75px; font-size: 20px; font-weight: 600; color: var(--brand); letter-spacing: -0.2px; }
  .specialty { left: 302px; top: 98px; font-size: 17px; color: var(--ink); }
  .contact { left: 302px; font-size: 16px; color: var(--ink); display: flex; align-items: center; gap: 7px; }
  .contact svg { width: 15px; height: 15px; flex: none; }
  .contact-phone { top: 135px; }
  .contact-email { top: 156px; }
  .contact-web { top: 177px; }
  .practice { left: 304px; top: 213px; font-size: 17px; color: var(--brand); }
  .address { left: 304px; font-size: 17px; color: var(--ink); }
  .address-street { top: 234px; }
  .address-city { top: 255px; }

  /* back */
  .back-circle {
    position: absolute; left: 164px; top: 52px; width: 252px; height: 252px;
    border-radius: 50%; background: var(--brand-faint);
  }
  .appointment-title {
    left: 0; width: 100%; text-align: center; top: 84px;
    font-size: 30px; font-weight: 600; color: var(--brand); padding-right: 10px;
  }
  .write-line { position: absolute; left: 137px; width: 316px; height: 1px; background: var(--rule); }
  .write-line-1 { top: 175px; }
  .write-line-2 { top: 227px; }
  .notice {
    left: 0; width: 100%; text-align: center; top: 310px; padding-right: 10px;
    font-size: 14px; font-style: italic; color: var(--muted);
  }
</style>
</head>
<body>
  <section class="card card-front">
    <div class="brand-circle"></div>
    <div class="abs brand-name">Marble Shore Dental</div>
    <div class="divider"></div>

    <div class="abs doctor">Nora T. Avery DDS</div>
    <div class="abs specialty">General Dentistry</div>

    <div class="abs contact contact-phone">
      <svg viewBox="0 0 16 16" aria-hidden="true"><path d="M4 1.5 6.2 4.3 5 6c.8 1.8 2.2 3.2 4 4l1.7-1.2 2.8 2.2-1.3 2.3C7 13.3 2.7 9 2.7 2.8Z" fill="none" stroke="var(--brand)" stroke-width="1.4" stroke-linejoin="round"/></svg>
      <span>555-014-2290</span>
    </div>
    <div class="abs contact contact-email">
      <svg viewBox="0 0 16 16" aria-hidden="true"><rect x="1" y="3.5" width="14" height="9.5" fill="var(--brand)"/><path d="M1 3.5 8 9l7-5.5" fill="none" stroke="#fff" stroke-width="1.2"/></svg>
      <span>info@marbleshoredental.example</span>
    </div>
    <div class="abs contact contact-web">
      <svg viewBox="0 0 16 16" aria-hidden="true"><g fill="none" stroke="var(--brand)" stroke-width="1.1"><circle cx="8" cy="8" r="6.5"/><ellipse cx="8" cy="8" rx="3" ry="6.5"/><path d="M1.5 8h13M2.5 4.8h11M2.5 11.2h11"/></g></svg>
      <span>www.marbleshoredental.example</span>
    </div>

    <div class="abs practice">Marble Shore Dental</div>
    <div class="abs address address-street">1820 Seabright Avenue</div>
    <div class="abs address address-city">Coral Bay, CA 90000</div>
  </section>

  <section class="card card-back">
    <div class="back-circle"></div>
    <div class="abs appointment-title">Your Next Appointment</div>
    <div class="write-line write-line-1"></div>
    <div class="write-line write-line-2"></div>
    <div class="abs notice">If you unable to keep appointment please give 24 hrs notice</div>
  </section>
</body>
</html>
```